Social Media Post Quote #1 - Native American Organization

- SOLVANE - must be included
- Protect your community. Protect Your Elders. Stay Vaccinated. must be included
- Attached, company Logo, campaign logos and sample flu social media image. - our audience likes BRIGHT colors.
- Must include image from the United States, representing Land/Nature from one of the following regions, Plains and Woodlands, or Southwest, or Mountains, or Coast, or Pow-wow.
- must include quote “Don’t let the flu interfere with our gatherings.” – Anonymous Tribal Member
- One image will be provided twice - incorporating campaign logos - in some fashion

```html
<!DOCTYPE html>
<html lang="en">
<head>
<meta charset="utf-8">
<title>SOLVANE – Protect Your Elders</title>
<link rel="stylesheet" href="https://fonts.googleapis.com/css2?family=Barlow:wght@400;500&family=Barlow+Condensed:wght@700&family=Roboto+Condensed:wght@400;700&display=swap">
<style>
  :root{
    --teal:#3e9aa6;
    --brick:#a6504a;
    --cream:#f2ede6;
    --white:#ffffff;
    --sky-top:#c9ccd0;
    --sky-mid:#e6ddd0;
    --glow:#f2a24a;
    --earth:#b5522c;
    --earth-deep:#6e2c1c;
  }
  *{margin:0;padding:0;box-sizing:border-box}
  html,body{width:1200px;height:1196px;overflow:hidden;background:var(--cream)}
  .post{position:relative;width:1200px;height:1196px;overflow:hidden}
  .border-band{position:absolute;inset:0;
    background:linear-gradient(135deg,var(--teal) 0%,var(--brick) 50%,var(--teal) 100%);opacity:.85}
  .border-inner{position:absolute;inset:12px;background:var(--cream)}
  .border-pattern{position:absolute;inset:14px;
    background:linear-gradient(90deg,rgba(62,154,166,.55),rgba(166,80,74,.55))}
  .landscape{position:absolute;left:40px;top:40px;width:1120px;height:1116px;
    background:linear-gradient(180deg,var(--cream) 0%,var(--sky-top) 22%,var(--sky-mid) 48%,var(--glow) 62%,var(--earth) 75%,var(--earth-deep) 100%)}

  .campaign-name{position:absolute;left:78px;top:92px;
    font-family:"Roboto Condensed",sans-serif;font-weight:700;font-size:78px;line-height:90px;
    letter-spacing:3px;color:var(--teal)}

  .partner-name{position:absolute;left:900px;top:178px;width:245px;
    font-family:"Roboto Condensed",sans-serif;font-weight:700;font-size:24px;line-height:28px;
    color:var(--brick);text-align:center;text-transform:uppercase}

  .headline{position:absolute;left:78px;top:252px;font-weight:400}
  .headline-line{position:relative;display:block;height:66px;background:var(--brick);
    box-shadow:10px 10px 0 var(--teal);color:var(--cream);
    font-family:"Roboto Condensed",sans-serif;font-weight:400;font-size:50px;line-height:66px;padding-left:14px;white-space:nowrap}
  .headline-line b{font-weight:700}
  .headline-line:nth-child(1){width:648px}
  .headline-line:nth-child(2){width:567px}
  .headline-line:nth-child(3){width:437px}

  .quote-frame{position:absolute;left:235px;top:576px;width:728px;height:370px}
  .quote-frame .panel{position:absolute;inset:0;background:rgba(90,55,40,.32)}
  .quote-frame svg{position:absolute;inset:0}
  .quote-mark{position:absolute;left:0;right:0;top:-80px;text-align:center;
    font-family:"Roboto Condensed",sans-serif;font-weight:700;font-size:210px;line-height:200px;color:var(--white)}
  .quote-text{position:absolute;left:0;right:0;top:66px;text-align:center;color:var(--white);
    font-family:"Barlow",sans-serif;font-weight:500;font-size:68px;line-height:82px;letter-spacing:-.5px}
  .quote-source{position:absolute;left:0;right:0;top:318px;text-align:center;color:var(--white);
    font-family:"Barlow",sans-serif;font-size:19px;letter-spacing:4.5px}
</style>
</head>
<body>
<main class="post">
  <div class="border-band"></div>
  <div class="border-inner"></div>
  <div class="border-pattern" role="img" aria-label="Woven chevron border in teal and brick red"></div>
  <div class="landscape" role="img" aria-label="Southwest desert buttes at sunset with a winding dirt road across red earth"></div>

  <div class="campaign-name">SOLVANE</div>

  <div class="partner-name">Northlight Elder Alliance</div>

  <h1 class="headline">
    <span class="headline-line"><b>PROTECT</b> YOUR COMMUNITY.</span>
    <span class="headline-line"><b>PROTECT</b> YOUR ELDERS.</span>
    <span class="headline-line"><b>STAY</b> VACCINATED.</span>
  </h1>

  <figure class="quote-frame">
    <div class="panel"></div>
    <svg width="728" height="370" viewBox="0 0 728 370" aria-hidden="true">
      <path d="M286 1.5 H1.5 V368.5 H726.5 V1.5 H442" fill="none" stroke="#ffffff" stroke-width="3"/>
    </svg>
    <div class="quote-mark">“</div>
    <blockquote class="quote-text">Don’t let the flu<br>interfere with our<br>gatherings.</blockquote>
    <figcaption class="quote-source">Anonymous Tribal Member</figcaption>
  </figure>
</main>
</body>
</html>
```